Landscape design build company door flyer

I would like this flyer to convey a high-level of professionalism for a company that is excellent with communication with their clients as well as a company that does incredible installations

Went on vacation/holiday

```html
<!DOCTYPE html>
<html lang="en">
<head>
<meta charset="UTF-8">
<title>Cedarline Builders – Paver Driveway Flyer</title>
<link href="https://fonts.googleapis.com/css2?family=Bebas+Neue&family=Rubik:wght@400;500;700&display=swap" rel="stylesheet">
<style>
  :root {
    --navy: #1d3a4a;
    --backdrop: #234a5c;
    --paper: #e5e5e6;
    --white: #ffffff;
    --ink: #1d3a4a;
  }
  * { margin: 0; padding: 0; box-sizing: border-box; }
  html, body { width: 900px; height: 1200px; overflow: hidden; }
  body { background: var(--backdrop); position: relative; font-family: "Rubik", sans-serif; }

  .flyer {
    position: absolute; left: 228px; top: 27px; width: 443px; height: 1145px;
    background: var(--paper); overflow: hidden;
    box-shadow: 0 4px 14px rgba(0,0,0,0.35);
  }
  .flyer-shapes { position: absolute; inset: 0; }

  .brand-badge {
    position: absolute; left: 21px; top: 25px; width: 104px; height: 104px;
    border-radius: 50%; background: var(--white);
    display: flex; align-items: center; justify-content: center; text-align: center;
  }
  .brand-name {
    font-family: "Rubik", sans-serif; font-weight: 500; font-size: 10.5px;
    color: var(--ink); letter-spacing: 0.3px; line-height: 1.2;
  }

  .headline {
    position: absolute; left: 0; right: 0; top: 386px;
    font-family: "Bebas Neue", sans-serif; font-size: 44px; line-height: 43px;
    color: var(--ink); text-align: center; letter-spacing: 0.3px;
  }

  .project-photo {
    position: absolute; border-radius: 50%; border: 4px solid var(--navy);
  }
  .project-photo--pavilion { left: 14px; top: 559px; width: 144px; height: 144px;
    background: linear-gradient(170deg, #9ab4c9 0%, #c69a62 35%, #6a6560 70%, #8a8f7a 100%); }
  .project-photo--patio { left: 20px; top: 735px; width: 174px; height: 174px;
    background: linear-gradient(175deg, #8fb6d6 0%, #b58a5c 35%, #4c4f55 62%, #9a9c8c 100%); }
  .project-photo--deck { left: 182px; top: 852px; width: 206px; height: 206px;
    background: linear-gradient(160deg, #3f5a78 0%, #2f4257 45%, #7d6048 70%, #6c7a5a 100%); }

  .intro {
    position: absolute; left: 184px; top: 563px; width: 221px;
    font-size: 14px; line-height: 20.3px; color: var(--ink);
    text-align: justify; text-align-last: center; letter-spacing: 0.2px;
  }

  .cta {
    position: absolute; left: 208px; top: 785px; width: 195px; height: 39px;
    background: var(--navy); color: var(--white);
    font-weight: 700; font-size: 15.5px; display: flex; align-items: center; justify-content: center;
    letter-spacing: 0.1px;
  }

  .tagline {
    position: absolute; left: 20px; top: 944px; width: 156px;
    font-weight: 500; font-size: 14px; line-height: 17.4px; color: var(--ink); text-align: center;
  }

  .contact-label {
    position: absolute; left: 19px; top: 1081px;
    font-family: "Bebas Neue", sans-serif; font-size: 16px; color: var(--white); letter-spacing: 0.3px;
  }
  .contact-phone {
    position: absolute; left: 18px; top: 1095px;
    font-family: "Bebas Neue", sans-serif; font-size: 32px; color: var(--white); letter-spacing: 0.4px;
  }
  .contact-web {
    position: absolute; right: 24px; top: 1110px;
    font-family: "Bebas Neue", sans-serif; font-size: 16px; color: var(--white); letter-spacing: 0.2px;
  }
</style>
</head>
<body>
  <main class="flyer">
    <svg class="flyer-shapes" width="443" height="1145" viewBox="0 0 443 1145" aria-hidden="false">
      <defs>
        <linearGradient id="heroTones" x1="0" y1="0" x2="0" y2="1">
          <stop offset="0" stop-color="#9fc2dd"/>
          <stop offset="0.3" stop-color="#c08a52"/>
          <stop offset="0.6" stop-color="#4f5658"/>
          <stop offset="1" stop-color="#6f7270"/>
        </linearGradient>
      </defs>
      <path role="img" aria-label="Photo of a covered outdoor pavilion with stone fireplace and bar"
            fill="url(#heroTones)"
            d="M0,0 H443 V195 C390,205 340,240 270,280 C200,318 100,315 0,265 Z"/>
      <path class="wave-top" fill="var(--navy)"
            d="M0,270 C60,335 150,360 230,330 C300,305 350,260 443,265 V198 C390,210 340,245 270,285 C200,323 100,320 0,268 Z"/>
      <path class="wave-top-edge" fill="none" stroke="var(--white)" stroke-width="3"
            d="M0,268 C100,320 200,323 270,285 C340,245 390,210 443,198"/>
      <path class="wave-bottom" fill="var(--navy)"
            d="M443,944 C410,960 400,1000 380,1030 C350,1070 280,1078 200,1063 C120,1048 50,1055 0,1072 V1145 H443 Z"/>
    </svg>

    <div class="brand-badge">
      <span class="brand-name">CEDARLINE<br>BUILDERS</span>
    </div>

    <h1 class="headline">Elevate your driveway<br>with a premium paver<br>installation</h1>

    <div class="project-photo project-photo--pavilion" role="img" aria-label="Photo of a cedar pavilion with stone outdoor kitchen"></div>
    <div class="project-photo project-photo--patio" role="img" aria-label="Photo of a covered patio lounge beside a home"></div>
    <div class="project-photo project-photo--deck" role="img" aria-label="Photo of an elevated deck with black railings and stairs"></div>

    <p class="intro">Introducing the perfect enhancement for your home exterior: an expertly crafted paver driveway. If you’re interested in elevating the curb appeal of your property with a touch of elegance and sophistication that only a paver driveway can bring, then keep reading!</p>

    <div class="cta">GET A FREE ESTIMATE</div>

    <p class="tagline">It’s Time to Enhance Your Home Curb Appeal and Durability</p>

    <p class="contact-label">Call us now</p>
    <p class="contact-phone">(555) 014-2763</p>
    <p class="contact-web">WWW.CEDARLINEBUILDERS.COM</p>
  </main>
</body>
</html>
```